Labels for probiotic care products as Body Cream, Shower gel, Hand soap, ....

We are a starting a business in Flanders Belgium. We are looking for a label for care products, based on probiotics or good bacterie. We are looking for a fresh design that attracts people who wants a good product, based on naturally components. The products make that the microflora of the skin becomes and remains natural. The label must we be adaptive on bottles of 15 cm height to 8 cm height and a width of 4,5 cm. The brand name is KOLA EMU (beautiful skin in Hawaiian) or maybe just KOLA.

Industry/Entity Type

Business

Colors

Designer to choose colors to be used in the design.

Requirements
Must have
• somewhere the text "Probiotic Skin Care"
• I also have to tell that the bottles are white.
Nice to have
• I uploaded the 9 existing labels, but I want a totally new one, because the labels of our cleaning products are the same. I also uploaded a mood bord of labels I like.

```html
<!DOCTYPE html>
<html lang="en">
<head>
<meta charset="utf-8">
<title>KOLA EMU — Probiotic Skin Care Labels</title>
<link href="https://fonts.googleapis.com/css2?family=Oswald:wght@500&family=Montserrat:wght@600&display=swap" rel="stylesheet">
<style>
  :root {
    --bg-centre: #fdfef4;
    --bg-edge: #f6f9d9;
    --label: #a68eae;
    --label-box: #a98fb1;
    --ink: #ffffff;
  }
  html, body {
    margin: 0;
    padding: 0;
    width: 1200px;
    height: 979px;
    overflow: hidden;
  }
  body {
    position: relative;
    background: radial-gradient(ellipse at 50% 48%, var(--bg-centre) 0%, var(--bg-edge) 80%);
    font-family: "Oswald", sans-serif;
  }
  .label {
    position: absolute;
    background: var(--label);
    color: var(--ink);
    box-sizing: border-box;
  }
  .label--box { background: var(--label-box); }

  .brand {
    position: absolute;
    left: 0;
    right: 0;
    display: flex;
    justify-content: center;
    align-items: center;
    font-family: "Oswald", sans-serif;
    font-weight: 500;
    line-height: 1;
    white-space: nowrap;
  }
  .brand-mark {
    display: inline-block;
    background: var(--ink);
    flex: none;
  }
  .product-name {
    position: absolute;
    left: 0;
    right: 0;
    text-align: center;
    font-family: "Oswald", sans-serif;
    font-weight: 500;
    line-height: 1;
    white-space: nowrap;
  }
  .tagline {
    position: absolute;
    left: 0;
    right: 0;
    text-align: center;
    font-family: "Montserrat", sans-serif;
    font-weight: 600;
    white-space: nowrap;
    line-height: 1;
  }

  /* Tall bottle label */
  .label--tall { left: 78px; top: 311px; width: 206px; height: 467px; }
  .label--tall .brand { top: 96px; font-size: 26px; letter-spacing: 1px; gap: 9px; }
  .label--tall .brand-mark { width: 9px; height: 9px; }
  .label--tall .product-name { top: 340px; font-size: 22px; letter-spacing: 5px; padding-left: 5px; }
  .label--tall .tagline { top: 374px; font-size: 6.5px; letter-spacing: 2px; padding-left: 2px; }

  /* Box face */
  .label--box { left: 354px; top: 372px; width: 420px; height: 323px; }
  .label--box .brand { top: 102px; font-size: 26px; letter-spacing: 1px; gap: 9px; }
  .label--box .brand-mark { width: 9px; height: 9px; }
  .label--box .product-name { top: 199px; font-size: 28px; letter-spacing: 6px; padding-left: 6px; }
  .label--box .tagline { top: 238px; font-size: 6.5px; letter-spacing: 2px; padding-left: 2px; }

  /* Small dropper label */
  .label--small { left: 972px; top: 533px; width: 157px; height: 196px; }
  .label--small .brand { top: 34px; font-size: 18px; letter-spacing: 0.8px; gap: 6px; }
  .label--small .brand-mark { width: 6px; height: 6px; }
  .label--small .product-name { top: 140px; font-size: 13px; letter-spacing: 3px; padding-left: 3px; }
  .label--small .tagline { top: 162px; font-size: 5px; letter-spacing: 1.4px; padding-left: 1.4px; }
</style>
</head>
<body>
  <section class="label label--tall" aria-label="Tall bottle label">
    <div class="brand"><span class="brand-mark"></span><span class="brand-name">KOLA EMU</span></div>
    <div class="product-name">SKIN REPAIR</div>
    <div class="tagline">PROBIOTIC SKIN CARE</div>
  </section>

  <section class="label label--box" aria-label="Box front label">
    <div class="brand"><span class="brand-mark"></span><span class="brand-name">KOLA EMU</span></div>
    <div class="product-name">SKIN REPAIR</div>
    <div class="tagline">PROBIOTIC SKIN CARE</div>
  </section>

  <section class="label label--small" aria-label="Dropper bottle label">
    <div class="brand"><span class="brand-mark"></span><span class="brand-name">KOLA EMU</span></div>
    <div class="product-name">SKIN REPAIR</div>
    <div class="tagline">PROBIOTIC SKIN CARE</div>
  </section>
</body>
</html>
```